Web Design Project

Looking for a simple, yet creative, small company website that can grow with me. The company name is Dorvel Solutions and the first products will be branded as TorraWarm warmers.

The first product I am selling are small reusable sodium acetate warming pads directed to two markets. 1) outdoor sporting/hunting activities and 2) spa/heat therapy. Three different sizes of warmers are currently availaible.

One differentiating aspect of our product is a custom designed neoprene insulating sleeve into which the warmer fits so that it stays warmer longer.

Looking for a website that is simple, easy to navigate and fun.

I would like to be able to sell items directly from website and direct to Quillmart as well.

I have a logo to base your ideas on.

Pictures of the first three products. Please incorporate.

Requirements
Must have
• selling cart
contact page
how they work
Nice to have
• product video, may be added later

```html
<!DOCTYPE html>
<html lang="en">
<head>
<meta charset="utf-8">
<title>TorraWarm – Sodium Acetate Warming Pads</title>
<link href="https://fonts.googleapis.com/css2?family=Ubuntu:wght@300;400;500;700&family=Source+Sans+3:ital,wght@0,400;0,600;1,400&family=Oswald:wght@500&display=swap" rel="stylesheet">
<style>
:root{
  --red:#b31b2f;
  --red-dark:#8f1222;
  --ink:#1f1f1f;
  --text:#5f5f5f;
  --muted:#777;
  --line:#dcdcdc;
  --page-bg:#ebebeb;
  --sheet:#ffffff;
  --soft:#f2f2f2;
}
*{box-sizing:border-box;margin:0;padding:0}
html,body{width:1037px;height:1200px;overflow:hidden;background:var(--page-bg)}
.canvas{position:relative;width:1037px;height:1200px;overflow:hidden;background:var(--page-bg)}
.page{position:absolute;left:0;top:0;width:1090px;height:1261px;transform:scale(.9514);transform-origin:0 0;font-family:"Source Sans 3",Arial,sans-serif;color:var(--text)}
.abs{position:absolute}
.sheet{left:32px;top:13px;width:1024px;height:1145px;background:var(--sheet);border-radius:3px;box-shadow:0 0 6px rgba(0,0,0,.08)}

/* header */
.utility{left:736px;top:25px;width:297px;height:41px;background:var(--soft);border-radius:4px;font-size:12px;color:var(--muted)}
.utility span{position:absolute;top:12px;display:flex;align-items:center;gap:5px;white-space:nowrap}
.utility svg{fill:#8d8d8d}
.brand{left:62px;top:60px;display:flex;align-items:center;gap:12px}
.brand-mark{width:62px;height:64px;border-radius:10px;background:var(--red)}
.brand-name{font-family:"Ubuntu",sans-serif;font-weight:700;font-size:36px;color:var(--ink);letter-spacing:-.5px}
.main-nav{top:108px;font-family:"Ubuntu",sans-serif;font-size:16px;color:var(--red);white-space:nowrap}
.nav-sep{top:107px;width:1px;height:22px;background:var(--line)}

/* hero */
.hero{left:53px;top:152px;width:983px;height:376px;border:1px solid var(--line);border-radius:4px;background:radial-gradient(ellipse at 50% 40%,#fff 55%,#f1f1f1 100%)}
.hero-title{left:95px;top:202px;font-family:"Ubuntu",sans-serif;font-weight:400;font-size:29px;color:var(--red);white-space:nowrap}
.hero-sub{left:97px;top:240px;font-family:"Ubuntu",sans-serif;font-size:21px;color:var(--ink);white-space:nowrap}
.hero-copy{left:96px;top:271px;width:410px;font-size:13px;line-height:23px}
.hero-list{left:101px;top:328px;list-style:none;font-size:13px;font-style:italic;line-height:23.5px}
.hero-list li{padding-left:13px;position:relative}
.hero-list li::before{content:"";position:absolute;left:0;top:9px;border-left:4px solid #aaa;border-top:3px solid transparent;border-bottom:3px solid transparent}
.btn{top:421px;height:34px;width:116px;border-radius:3px;font-family:"Oswald",sans-serif;font-weight:500;font-size:14px;color:#fff;display:flex;align-items:center;justify-content:center;letter-spacing:.2px}
.btn-buy{left:96px;background:linear-gradient(#c42538,var(--red-dark))}
.btn-more{left:222px;background:linear-gradient(#3a3a3a,#0d0d0d)}
.hero-photo{left:573px;top:205px;width:428px;height:270px;background:#fff;border-radius:3px;box-shadow:0 1px 6px rgba(0,0,0,.15);padding:8px}
.hero-photo div{width:100%;height:100%;background:linear-gradient(160deg,#ffffff 20%,#efe8d8 55%,#e6e6e6 100%)}
.dot{top:505px;width:10px;height:10px;border-radius:50%;background:#cfcfcf}

/* content */
h2{position:absolute;font-family:"Ubuntu",sans-serif;font-weight:400;font-size:20px;color:var(--ink);white-space:nowrap}
.copy{position:absolute;font-size:13px;line-height:20px}
.copy p+p{margin-top:10px}
.copy strong{font-weight:600;color:#555}
.video{left:690px;top:589px;width:317px;height:213px;background:#d4d4d4;padding:7px}
.video-still{width:100%;height:100%;background:linear-gradient(135deg,#d9d4c9,#ece8df 45%,#c9c3b6 70%,#a9b78a 100%)}
.video svg{position:absolute;left:134px;top:75px}
.rule-h{left:59px;top:829px;width:977px;height:1px;background:var(--line)}
.rule-v{left:621px;top:830px;width:1px;height:303px;background:var(--line)}
.why-photo{left:59px;top:900px;width:136px;height:153px;background:linear-gradient(160deg,#6a5a44,#c0793b 45%,#4a6a9a 80%)}
.latest{color:var(--red)}
.card{width:186px;height:114px;border:1px solid var(--line);border-radius:3px;background:#fff}
.card div{margin:4px;height:104px}
.card-1 div{background:linear-gradient(#fff 40%,#2a2a2a 60%,#fff 85%)}
.card-2 div{background:linear-gradient(150deg,#f5f3e6,#e2dfca 60%,#cfcfc8)}
.prod-name{font-size:13px;color:var(--red);white-space:nowrap}
.prod-desc{font-size:12px;line-height:18px;color:var(--red);width:180px}
.prod-link{font-family:"Oswald",sans-serif;font-weight:500;font-size:12px;color:var(--red);white-space:nowrap}

/* footer */
.foot{font-size:12px;color:#555;white-space:nowrap}
.foot-nav{top:1184px;font-size:13px;color:var(--red);white-space:nowrap}
.social{top:1215px;width:23px;height:23px;border-radius:3px;background:#9a9a9a}
</style>
</head>
<body>
<div class="canvas">
<div class="page">
  <div class="abs sheet"></div>

  <header>
    <div class="abs utility">
      <span style="left:28px"><svg width="20" height="16" viewBox="0 0 20 16"><path d="M0 1h3l3 9h10l2-7H5l-.6-2H0z"/><circle cx="7" cy="13.5" r="1.8"/><circle cx="15" cy="13.5" r="1.8"/></svg>My Cart</span>
      <span style="left:117px"><svg width="14" height="18" viewBox="0 0 14 18"><path d="M3 8V5a4 4 0 0 1 8 0v1H9V5a2 2 0 0 0-4 0v3h8v10H1V8z"/></svg>Log In</span>
      <span style="left:191px"><svg width="16" height="18" viewBox="0 0 16 18"><circle cx="8" cy="5" r="4"/><path d="M0 18c0-5 3-8 8-8s8 3 8 8z"/></svg>My Account</span>
    </div>

    <div class="abs brand"><div class="brand-mark"></div><span class="brand-name">TorraWarm</span></div>

    <nav>
      <span class="abs main-nav" style="left:476px">Main</span>
      <span class="abs nav-sep" style="left:527px"></span>
      <span class="abs main-nav" style="left:547px">About Us</span>
      <span class="abs nav-sep" style="left:627px"></span>
      <span class="abs main-nav" style="left:647px">Products</span>
      <span class="abs nav-sep" style="left:723px"></span>
      <span class="abs main-nav" style="left:744px">Testimonials</span>
      <span class="abs nav-sep" style="left:847px"></span>
      <span class="abs main-nav" style="left:867px">Support</span>
      <span class="abs nav-sep" style="left:940px"></span>
      <span class="abs main-nav" style="left:959px">Contact</span>
    </nav>
  </header>

  <section>
    <div class="abs hero"></div>
    <h1 class="abs hero-title">Buy Sodium Acetate Warming Pads</h1>
    <p class="abs hero-sub">Integer tristique vitae consequat nec</p>
    <p class="abs hero-copy">Curabitur tristique mi condimentum orci. Mauris vel lacus vitae felis vestibulum volutpat. Etiam est nunc, venenatis in.</p>
    <ul class="abs hero-list">
      <li>Phasellus pellentesque aliquam enim.</li>
      <li>Proin dui lectus cursus eu.</li>
      <li>Mattis laoreet viverra sit amet quam.</li>
    </ul>
    <span class="abs btn btn-buy">BUY PRODUCT</span>
    <span class="abs btn btn-more">LEARN MORE</span>
    <div class="abs hero-photo"><div role="img" aria-label="Photo of two folded warming pads with hand controllers"></div></div>
    <span class="abs dot" style="left:517px"></span>
    <span class="abs dot" style="left:532px"></span>
    <span class="abs dot" style="left:546px"></span>
    <span class="abs dot" style="left:561px"></span>
  </section>

  <section>
    <h2 style="left:59px;top:557px">Welcome to Our Website Mainpage</h2>
    <div class="copy" style="left:61px;top:593px;width:600px">
      <p><strong>Mauris vel lacus vitae felis vestibulum volutpat. Etiam est nunc, venenatis in, tristique eu, imperdiet ac, nisl. Cum sociis natoque penatibus et magnis dis parturient montes</strong></p>
      <p>Phasellus felis dolor, scelerisque a, tempus eget, lobortis id, libero. Donec scelerisque leo ac risus. Praesent sit amet est. In dictum, dolor eu dictum porttitor, enim felis viverra mi, eget luctus massa purus quis odio. Etiam nulla massa, pharetra facilisis, volutpat in, imperdiet sit amet, sem.</p>
      <p>Aliquam nec erat at purus cursus interdum. Vestibulum ligula augue, bibendum accumsan, vestibulum ut, commodo a, mi. Morbi ornare gravida elit. Integer congue, augue et malesuada iaculis, ipsum dui aliquet felis, at cursus magna nisl nec elit. Donec iaculis diam a nisi accumsan viverra.</p>
    </div>

    <h2 style="left:690px;top:556px">How it Works</h2>
    <div class="abs video">
      <div class="video-still" role="img" aria-label="Video still of a warming pad in its insulating sleeve"></div>
      <svg width="60" height="60" viewBox="0 0 60 60"><circle cx="30" cy="30" r="27" fill="none" stroke="#111" stroke-width="3.5"/><path d="M24 20l16 10-16 10z" fill="#111"/></svg>
    </div>
  </section>

  <div class="abs rule-h"></div>
  <div class="abs rule-v"></div>

  <section>
    <h2 style="left:58px;top:859px">Why Choose Our Product?</h2>
    <div class="abs why-photo" role="img" aria-label="Photo of feet in socks warming by a fireplace"></div>
    <div class="copy" style="left:211px;top:895px;width:392px">
      <p><strong>Class aptent taciti sociosqu ad litora torquent per conubia nostra, per inceptos hymenaeos.</strong> Proin nulla arcu, nonummy luctus, dictum eget, fermentum et, lorem. Nunc porta convallis pede.</p>
      <p>Mauris vel lacus vitae felis vestibulum volutpat. Etiam est nunc, venenatis in, tristique eu, imperdiet ac, nisl. Cum sociis natoque penatibus et magnis dis parturient montes, nascetur ridiculus mus. In iaculis facilisis massa. Etiam eu urna.</p>
      <p>Sed porta. Suspendisse quam leo, molestie sed, luctus quis, feugiat in, pede. Fusce tellus. Sed metus augue, convallis et, vehicula ut.</p>
    </div>
  </section>

  <section>
    <h2 class="latest" style="left:640px;top:859px">Latest Products</h2>

    <div class="abs card card-1" style="left:639px;top:894px"><div role="img" aria-label="Photo of feet resting on a black heated floor mat"></div></div>
    <span class="abs prod-name" style="left:639px;top:1019px">Product Name here</span>
    <p class="abs prod-desc" style="left:639px;top:1036px">Fusce tellus. Sed metus augue, convallis et, vehicula ut, pulvinar.</p>
    <span class="abs prod-link" style="left:640px;top:1079px">LEARN MORE ›</span>

    <div class="abs card card-2" style="left:847px;top:895px"><div role="img" aria-label="Photo of a cream heated pad with controller"></div></div>
    <span class="abs prod-name" style="left:849px;top:1020px">Product Name here</span>
    <p class="abs prod-desc" style="left:849px;top:1039px">Fusce tellus. Sed metus augue, convallis et, vehicula ut, pulvinar.</p>
    <span class="abs prod-link" style="left:850px;top:1080px">LEARN MORE ›</span>
  </section>

  <footer>
    <span class="abs foot" style="left:37px;top:1182px">Copyright © 2012 Company Name.&nbsp; All right reserved.</span>
    <span class="abs foot" style="left:39px;top:1209px">Priacy Policy&nbsp; |&nbsp; Term &amp; Conditions</span>
    <span class="abs foot-nav" style="left:618px">Main&nbsp;&nbsp;&nbsp; |&nbsp;&nbsp;&nbsp; About Us&nbsp;&nbsp;&nbsp; |&nbsp;&nbsp;&nbsp; Products&nbsp;&nbsp;&nbsp; |&nbsp;&nbsp;&nbsp; Testimonials&nbsp;&nbsp;&nbsp; |&nbsp;&nbsp;&nbsp; Support&nbsp;&nbsp;&nbsp; |&nbsp;&nbsp;&nbsp; Contact</span>
    <span class="abs social" style="left:944px"></span>
    <span class="abs social" style="left:972px"></span>
    <span class="abs social" style="left:1001px"></span>
    <span class="abs social" style="left:1030px"></span>
  </footer>
</div>
</div>
</body>
</html>
```